Software static HTML page design

We need 5 static HTML pages designed for our current software startup - TallyNest. All details are attached in a document for consideration.

Target Market(s)

Sporting clubs/University clubs

Industry/Entity Type

Software

Number of Pages Required

5+ page

Font styles to use
Sans Serif

Colors
33a6d7
85cae6
86cfc6
33b8a4
ffffff

```html
<!DOCTYPE html>
<html lang="en">
<head>
<meta charset="utf-8">
<title>TallyNest – Bringing your club to the social web</title>
<link href="https://fonts.googleapis.com/css2?family=Lato:wght@300;400;700;900&display=swap" rel="stylesheet">
<style>
:root{
  --blue:#33a6d7;
  --blue-light:#85cae6;
  --mint:#86cfc6;
  --teal:#33b8a4;
  --white:#ffffff;
  --ink:#2b2b2b;
  --ink-soft:#555b61;
  --grey:#8a9096;
  --line:#dde1e4;
  --dark:#262626;
  --darker:#1d1d1d;
  --slate:#3a3c3e;
  --slate-light:#8a8d90;
}
*{box-sizing:border-box;margin:0;padding:0}
html,body{width:1200px;height:5140px;overflow:hidden}
body{font-family:"Lato",sans-serif;color:var(--ink);background:var(--white);position:relative}
section,header,footer{position:absolute;left:0;width:1200px}
.abs{position:absolute}
.eyebrow{font-size:14px;letter-spacing:1px;text-transform:uppercase;color:var(--grey);text-align:center}
.section-title{font-size:27px;font-weight:900;text-transform:uppercase;text-align:center;letter-spacing:.5px}
.btn{display:inline-block;background:var(--teal);color:var(--white);font-weight:700;font-size:17px;text-transform:uppercase;text-align:center;letter-spacing:.5px}
.brand{font-weight:900;font-size:30px;color:var(--white);letter-spacing:.5px}

/* Hero */
.hero{top:0;height:600px;background:linear-gradient(180deg,#3c4146 0%,#2d3236 55%,#5a6064 100%)}
.nav{position:absolute;top:26px;left:0;width:1200px;height:50px}
.nav .brand{position:absolute;left:40px;top:6px}
.nav-links{position:absolute;left:312px;top:14px;display:flex;gap:26px;list-style:none}
.nav-links li{color:var(--white);font-size:16px;font-weight:700;letter-spacing:.5px}
.nav .signup{position:absolute;left:938px;top:0;width:186px;height:50px;line-height:50px}
.hero-device{left:42px;top:210px;width:500px;height:330px;background:linear-gradient(180deg,#f1f3f5,#cfd4d8);border:14px solid #1b1d20;border-radius:12px 12px 0 0}
.hero-device-base{left:0;top:532px;width:586px;height:22px;background:linear-gradient(180deg,#c9cdd1,#8d9297);border-radius:0 0 18px 18px}
.hero-title{left:604px;top:258px;color:var(--white)}
.hero-title h1{font-size:42px;font-weight:900;letter-spacing:1px;line-height:1.1}
.hero-title p{font-size:27px;font-weight:900;letter-spacing:1px;margin-top:4px}
.hero .know{left:604px;top:402px;width:196px;height:58px;line-height:58px;font-size:22px}
.dots{left:620px;top:516px;display:flex;gap:22px}
.dots span{width:14px;height:14px;border-radius:50%;background:rgba(255,255,255,.45)}
.dots span:first-child{background:var(--white)}

/* Features */
.features{top:600px;height:628px}
.features .eyebrow{position:absolute;top:64px;width:100%}
.features .section-title{position:absolute;top:92px;width:100%;font-size:24px}
.feature{position:absolute;width:300px;display:flex;gap:20px}
.feature-icon{width:48px;height:48px;flex:none}
.feature h3{font-size:17px;font-weight:700;margin-bottom:8px}
.feature p{font-size:13px;color:var(--grey);line-height:1.45;width:200px}
.tablet{left:430px;top:276px;width:340px;height:236px;background:#17191c;border-radius:18px;padding:16px}
.tablet .screen{width:100%;height:100%;background:linear-gradient(135deg,#f3f6f8,#d9eef0);border-radius:4px}
.features .view-all{left:470px;top:540px;width:244px;height:56px;line-height:56px;font-size:16px}

/* Tour */
.tour{top:1228px;height:632px;background:linear-gradient(180deg,var(--blue) 0%,#29b2e6 100%)}
.tour .eyebrow{position:absolute;top:22px;width:100%;color:rgba(255,255,255,.75)}
.tour .section-title{position:absolute;top:48px;width:100%;color:var(--white);font-size:25px}
.tour-side{top:128px;height:500px;width:100px;background:linear-gradient(180deg,#2d2d2d,#151515)}
.tour-side.left{left:0}
.tour-side.right{left:1100px}
.tour-video{left:184px;top:128px;width:856px;height:500px;background:linear-gradient(160deg,#4a4d50 0%,#26282a 60%,#1a1b1c 100%)}
.tour-play{left:556px;top:330px;width:90px;height:64px}

/* Pricing */
.pricing{top:1860px;height:844px}
.pricing .eyebrow{position:absolute;top:76px;width:100%}
.pricing .section-title{position:absolute;top:100px;width:100%;font-size:25px}
.plan{position:absolute;width:298px;height:440px;background:var(--white);box-shadow:0 2px 12px rgba(0,0,0,.18)}
.plan-band{position:absolute;left:0;top:0;width:100%;height:170px}
.starter .plan-band{background:linear-gradient(180deg,var(--teal) 0%,var(--teal) 55%,var(--mint) 100%)}
.pro .plan-band{background:linear-gradient(180deg,var(--blue) 0%,var(--blue) 55%,var(--blue-light) 100%)}
.business .plan-band{background:linear-gradient(180deg,var(--slate) 0%,var(--slate) 55%,var(--slate-light) 100%)}
.plan-head{position:absolute;left:0;top:22px;width:100%;text-align:center;color:var(--white)}
.plan-head h3{font-size:26px;font-weight:700;text-transform:uppercase;letter-spacing:.5px}
.plan-head p{font-size:26px;font-weight:400;margin-top:4px}
.plan ul{list-style:none;position:absolute;left:28px;top:220px}
.plan li{font-size:13px;text-transform:uppercase;color:var(--ink-soft);line-height:34px;letter-spacing:.3px}
.plan.starter{left:122px;top:270px}
.plan.pro{left:460px;top:212px}
.plan.business{left:800px;top:270px}

/* Testimonial */
.testimonial{top:2704px;height:436px;background:var(--dark);color:var(--white)}
.quote{position:absolute;left:180px;top:80px;width:840px;text-align:center;font-size:17px;font-style:italic;line-height:1.65}
.quote-mark{position:absolute;top:82px;width:32px;height:24px}
.person{position:absolute;left:0;top:224px;width:100%;text-align:center}
.person strong{display:block;font-size:14px;font-weight:700}
.person span{font-size:12px;color:#9aa0a5}
.avatar{position:absolute;border-radius:50%;background:linear-gradient(135deg,#6c6f72,#3b3e41)}

/* Blog */
.blog{top:3140px;height:860px}
.blog .eyebrow{position:absolute;top:76px;width:100%}
.blog .section-title{position:absolute;top:100px;width:100%;font-size:25px}
.post{position:absolute;top:240px;width:355px}
.post-image{width:355px;height:322px}
.post h3{font-size:19px;font-weight:400;margin-top:26px}
.post p{font-size:14px;color:var(--grey);line-height:1.5;margin-top:10px}
.post-meta{display:flex;justify-content:space-between;border-top:1px solid var(--line);margin-top:10px;padding-top:6px;font-size:12px;color:var(--grey)}
.post-meta .author{color:var(--mint)}

/* Newsletter */
.newsletter{top:4000px;height:124px;background:linear-gradient(90deg,#2bbbe6,var(--blue))}
.newsletter h2{position:absolute;left:80px;top:46px;color:var(--white);font-size:22px;font-weight:900;text-transform:uppercase;letter-spacing:.5px}
.newsletter .subscribe{position:absolute;left:848px;top:32px;width:206px;height:60px;line-height:60px;background:var(--white);color:var(--ink);font-size:17px;font-weight:700;text-transform:uppercase;text-align:center}

/* Contact */
.contact{top:4124px;height:640px}
.map{left:0;top:0;width:600px;height:640px;background:linear-gradient(150deg,#e7e3dc 0%,#d8e8ee 45%,#9fc7e4 70%,#e6e1d8 100%)}
.contact h2{position:absolute;left:622px;top:68px;font-size:25px;font-weight:900;text-transform:uppercase;letter-spacing:.5px}
.field{position:absolute;border:1px solid #b8bdc1;height:64px;padding:18px 16px;font-size:15px;color:var(--ink-soft)}
.contact .submit{left:622px;top:538px;width:160px;height:58px;line-height:58px;font-size:20px}

/* Footer */
.footer{top:4764px;height:326px;background:var(--darker);color:var(--white)}
.footer .brand{position:absolute;left:40px;top:54px}
.footer-col{position:absolute;top:60px;list-style:none}
.footer-col li{font-size:16px;line-height:36px}
.contact-list{position:absolute;left:862px;top:56px;list-style:none}
.contact-list li{display:flex;gap:16px;font-size:16px;line-height:22px;margin-bottom:16px}
.contact-list svg{flex:none;margin-top:2px}
.social{position:absolute;left:846px;top:254px;display:flex;gap:24px}
.social span{width:40px;height:40px;border-radius:50%;background:var(--white)}
.legal{top:5090px;height:50px;text-align:center;font-size:15px;line-height:50px;color:var(--ink)}
</style>
</head>
<body>

<header class="hero">
  <div class="abs" style="inset:0" role="img" aria-label="Dusky city skyline photo behind the hero"></div>
  <nav class="nav">
    <div class="brand">TallyNest</div>
    <ul class="nav-links">
      <li>HOME</li><li>FEATURES</li><li>PRICING</li><li>CONTACT</li><li>LOGIN</li>
    </ul>
    <span class="btn signup">Sign up</span>
  </nav>
  <div class="abs hero-device" role="img" aria-label="Laptop showing the TallyNest club dashboard"></div>
  <div class="abs hero-device-base"></div>
  <div class="abs hero-title">
    <h1>BRINGING YOUR CLUB</h1>
    <p>TO THE SOCIAL WEB</p>
  </div>
  <span class="abs btn know">Know more</span>
  <div class="abs dots"><span></span><span></span></div>
</header>

<section class="features">
  <p class="eyebrow">Core features</p>
  <h2 class="section-title">The features of best ever</h2>

  <div class="feature" style="left:82px;top:244px">
    <svg class="feature-icon" viewBox="0 0 48 48"><rect x="6" y="8" width="36" height="30" rx="3" fill="none" stroke="var(--teal)" stroke-width="3"/><circle cx="18" cy="21" r="5" fill="var(--teal)"/><path d="M26 18h10M26 25h10M12 31h14" stroke="var(--teal)" stroke-width="3"/></svg>
    <div><h3>Contact Information</h3><p>Keep every member detail in one tidy place.</p></div>
  </div>
  <div class="feature" style="left:82px;top:358px">
    <svg class="feature-icon" viewBox="0 0 48 48"><rect x="8" y="8" width="32" height="34" rx="3" fill="none" stroke="var(--teal)" stroke-width="3"/><path d="M8 17h32M15 24h18M15 31h18" stroke="var(--teal)" stroke-width="3"/></svg>
    <div><h3>Team Schedule</h3><p>Plan training days and match fixtures with ease.</p></div>
  </div>
  <div class="feature" style="left:82px;top:470px">
    <svg class="feature-icon" viewBox="0 0 48 48"><path d="M6 10h26v18H16l-8 7v-7H6z" fill="none" stroke="var(--teal)" stroke-width="3" stroke-linejoin="round"/><path d="M36 18h6v18h-4v6l-7-6H20v-4" fill="none" stroke="var(--teal)" stroke-width="3" stroke-linejoin="round"/></svg>
    <div><h3>TallyNest Live Chat</h3><p>Talk with your whole squad in real time.</p></div>
  </div>

  <div class="feature" style="left:860px;top:244px">
    <svg class="feature-icon" viewBox="0 0 48 48"><circle cx="24" cy="16" r="8" fill="none" stroke="var(--teal)" stroke-width="3"/><path d="M9 42c2-10 9-14 15-14s13 4 15 14" fill="none" stroke="var(--teal)" stroke-width="3"/></svg>
    <div><h3>Member Availability</h3><p>See who can play before every single game.</p></div>
  </div>
  <div class="feature" style="left:860px;top:358px">
    <svg class="feature-icon" viewBox="0 0 48 48"><rect x="8" y="10" width="32" height="30" rx="3" fill="none" stroke="var(--teal)" stroke-width="3"/><path d="M8 18h32M16 6v8M32 6v8M17 28l5 5 9-9" fill="none" stroke="var(--teal)" stroke-width="3"/></svg>
    <div><h3>TeamPulse Live!</h3><p>Share live scores and updates with every fan.</p></div>
  </div>
  <div class="feature" style="left:860px;top:470px">
    <svg class="feature-icon" viewBox="0 0 48 48"><path d="M8 10h32v22H22l-9 8v-8H8z" fill="none" stroke="var(--teal)" stroke-width="3" stroke-linejoin="round"/><circle cx="17" cy="21" r="2.5" fill="var(--teal)"/><circle cx="24" cy="21" r="2.5" fill="var(--teal)"/><circle cx="31" cy="21" r="2.5" fill="var(--teal)"/></svg>
    <div><h3>Track Payments</h3><p>Follow fees and dues paid across each season.</p></div>
  </div>

  <div class="abs tablet"><div class="screen" role="img" aria-label="Tablet showing the TallyNest analytics dashboard"></div></div>
  <span class="abs btn view-all">View all features</span>
</section>

<section class="tour">
  <p class="eyebrow">View us</p>
  <h2 class="section-title">Take a tour with us</h2>
  <div class="abs tour-side left" role="img" aria-label="Side preview of a club video"></div>
  <div class="abs tour-video" role="img" aria-label="Product tour video still of a hand holding a card"></div>
  <div class="abs tour-side right" role="img" aria-label="Side preview of a club video"></div>
  <svg class="abs tour-play" viewBox="0 0 90 64"><rect x="2" y="2" width="86" height="60" rx="6" fill="none" stroke="#fff" stroke-width="4"/><path d="M36 18v28l24-14z" fill="#fff"/></svg>
</section>

<section class="pricing">
  <p class="eyebrow">Flexible pricing</p>
  <h2 class="section-title">Grow your business</h2>

  <div class="plan starter">
    <div class="plan-band" role="img" aria-label="Teal wave decoration"></div>
    <div class="plan-head"><h3>Starter</h3><p>$16.00</p></div>
    <ul><li>Small</li><li>Agile state</li><li>Evolving methods</li><li>Customer support</li><li>Usable dashboard</li></ul>
  </div>

  <div class="plan pro">
    <div class="plan-band" role="img" aria-label="Blue wave decoration"></div>
    <div class="plan-head"><h3>Professional</h3><p>$32.00</p></div>
    <ul><li>Medium</li><li>Agile state</li><li>Evolving methods</li><li>Customer support</li><li>Usable dashboard</li></ul>
  </div>

  <div class="plan business">
    <div class="plan-band" role="img" aria-label="Charcoal wave decoration"></div>
    <div class="plan-head"><h3>Business</h3><p>$56.00</p></div>
    <ul><li>Large</li><li>Agile state</li><li>Evolving methods</li><li>Customer support</li><li>Usable dashboard</li></ul>
  </div>
</section>

<section class="testimonial">
  <svg class="quote-mark" style="left:128px" viewBox="0 0 40 30"><path d="M2 28V16C2 8 6 3 14 2v5c-4 1-6 4-6 8h6v13zM22 28V16c0-8 4-13 12-14v5c-4 1-6 4-6 8h6v13z" fill="var(--teal)"/></svg>
  <p class="quote">At vero eos et accusamus et iusto odio dignissimos ducimus qui blanditiis praesentium voluptatum deleniti atque corrupti quos dolores et quas molestias excepturi sint occaecati cupiditate non provident, similique sunt in culpa qui officia deserunt mollitia animi</p>
  <svg class="quote-mark" style="left:1040px" viewBox="0 0 40 30"><path d="M38 2v12c0 8-4 13-12 14v-5c4-1 6-4 6-8h-6V2zM18 2v12c0 8-4 13-12 14v-5c4-1 6-4 6-8H6V2z" fill="var(--teal)"/></svg>
  <div class="person"><strong>Mara Voss</strong><span>director</span></div>
  <div class="avatar" style="left:520px;top:312px;width:80px;height:80px" role="img" aria-label="Club member portrait"></div>
  <div class="avatar" style="left:588px;top:290px;width:108px;height:108px;border:4px solid #fff;background:linear-gradient(135deg,#c9a78a,#6d5140)" role="img" aria-label="Portrait of Mara Voss"></div>
  <div class="avatar" style="left:686px;top:312px;width:80px;height:80px" role="img" aria-label="Club member portrait"></div>
</section>

<section class="blog">
  <p class="eyebrow">Flexible pricing</p>
  <h2 class="section-title">Grow your business</h2>

  <article class="post" style="left:40px">
    <div class="post-image" style="background:linear-gradient(135deg,#0e2a3a,#0a1620)" role="img" aria-label="Code on a dark screen"></div>
    <h3>At vero eos et accusamus et</h3>
    <p>Sed ut perspiciatis unde omnis iste natus error sit voluptatem accusantium laudantium.</p>
    <div class="post-meta"><span class="author">Admin</span><span>12.08.2017</span></div>
  </article>
  <article class="post" style="left:423px">
    <div class="post-image" style="background:linear-gradient(135deg,#7e8a96,#3c4550)" role="img" aria-label="Laptop on a desk with coffee"></div>
    <h3>At vero eos et accusamus et</h3>
    <p>Sed ut perspiciatis unde omnis iste natus error sit voluptatem accusantium laudantium.</p>
    <div class="post-meta"><span class="author">Admin</span><span>12.08.2017</span></div>
  </article>
  <article class="post" style="left:806px">
    <div class="post-image" style="background:linear-gradient(135deg,#c6cfd6,#5d6873)" role="img" aria-label="Man working at a laptop in an office"></div>
    <h3>At vero eos et accusamus et</h3>
    <p>Sed ut perspiciatis unde omnis iste natus error sit voluptatem accusantium laudantium.</p>
    <div class="post-meta"><span class="author">Admin</span><span>12.08.2017</span></div>
  </article>
</section>

<section class="newsletter">
  <h2>Subscribe the newsletter for recive updates</h2>
  <span class="subscribe">Subscribe now</span>
</section>

<section class="contact">
  <div class="abs map" role="img" aria-label="Street map of the club's city by a river"></div>
  <h2>Get in touch</h2>
  <div class="field" style="left:622px;top:144px;width:254px">Name</div>
  <div class="field" style="left:886px;top:144px;width:254px">Phone</div>
  <div class="field" style="left:622px;top:232px;width:518px">E-mail</div>
  <div class="field" style="left:622px;top:320px;width:518px">Type of Club</div>
  <div class="field" style="left:622px;top:408px;width:518px;height:112px">Message</div>
  <span class="abs btn submit">Submit</span>
</section>

<footer class="footer">
  <div class="brand">TallyNest</div>
  <ul class="footer-col" style="left:516px"><li>About</li><li>Features</li><li>Pricing</li></ul>
  <ul class="footer-col" style="left:640px"><li>Login</li><li>Clients</li></ul>
  <ul class="contact-list">
    <li><svg width="20" height="20" viewBox="0 0 20 20"><path d="M5 2l3 4-2 2c1 2 3 4 5 5l2-2 4 3-2 4C9 18 2 11 2 5z" fill="#fff"/></svg>555-014-288</li>
    <li><svg width="20" height="20" viewBox="0 0 20 20"><rect x="2" y="4" width="16" height="12" fill="#fff"/><path d="M2 4l8 7 8-7" fill="none" stroke="#1d1d1d" stroke-width="1.5"/></svg>hello@tallynest.com</li>
    <li><svg width="20" height="20" viewBox="0 0 20 20"><path d="M10 1a6 6 0 0 0-6 6c0 5 6 12 6 12s6-7 6-12a6 6 0 0 0-6-6z" fill="#fff"/><circle cx="10" cy="7" r="2.2" fill="#1d1d1d"/></svg><span>48 Harbor Lane<br>Eastport, FL 30021</span></li>
  </ul>
  <div class="social"><span></span><span></span><span></span><span></span></div>
</footer>

<div class="abs legal" style="left:0;width:1200px">privacy policy &nbsp;|&nbsp; 2017@tallynest all right reserved</div>

</body>
</html>
```